Need a revamp of our website to attract larger companies and government authorities. The site must breathe that we are a company ready for larger projects both in the web and app sector. And also, that we can start projects with short notice.

Until now the design suggestions for us have been mor suitable for smaller firms but we have now taken the step in the larger/bigger range.

Most of our web nowadays has been work on digitalization of all kinds of administrative systems.

The site to be redone is https://brightquill.eu And that brand is a sub brand to https://tallmoor.se

startpage
servicelist presentation page
service detail page
caselist page (same as article list)
case detail page (same as article detail)
about us page
contact us page
Updates

We have this video that can be used as a hero banner video

https://www.filecrate.example/t/9QpLmZr4TxWbNvKc

Target Market(s)

b2b customers

Coding

Coded - Design and coding required

Number of Pages Required

5+ page

Font styles to use
Sans Serif

Requirements
Must have
• A thought throu theme. with details folowing the whole design www.pexanor.se
Nice to have
• maybe a video hero banner https://www.filecrate.example/t/9QpLmZr4TxWbNvKc
Should not have
• a standard theme look and feel.

```html
<!DOCTYPE html>
<html lang="en">
<head>
<meta charset="utf-8">
<title>Bright Quill – Web &amp; Mobile Apps</title>
<link href="https://fonts.googleapis.com/css2?family=Poppins:wght@300;400;500;600;700;800&display=swap" rel="stylesheet">
<style>
:root{
  --slate:#2f4a5a;
  --slate-deep:#2c4656;
  --grey:#8b95a1;
  --blue:#0aa1f0;
  --text:#55616c;
  --band:#eef0f4;
  --white:#fff;
  --line:#e3e6ea;
}
*{box-sizing:border-box;margin:0;padding:0}
html,body{width:1200px;height:3648px;overflow:hidden}
body{font-family:'Poppins',sans-serif;color:var(--text);background:var(--white);position:relative}
.abs{position:absolute}
a{color:inherit;text-decoration:none}

/* hero */
.hero{left:0;top:0;width:1200px;height:703px;background:linear-gradient(180deg,#8a7a5e 0%,#9a8a68 18%,#7f8a55 40%,#6f8c3f 62%,#87a04e 100%)}
.brand{left:88px;top:58px;color:var(--white);font-weight:600;font-size:17px;letter-spacing:.5px;display:flex;align-items:center;gap:8px}
.brand .dot{width:12px;height:12px;background:var(--white)}
.nav{left:511px;top:40px;display:flex;gap:32px;font-size:12px;font-weight:600;color:var(--white);letter-spacing:.2px}
.nav .active{position:relative}
.nav .active::before{content:"";position:absolute;left:-4px;right:-4px;top:-40px;height:3px;background:var(--white)}
.search{left:1065px;top:28px;width:44px;height:44px;border-radius:50%;background:rgba(255,255,255,.3);display:flex;align-items:center;justify-content:center}
.hero-card{left:89px;top:204px;width:350px;height:330px;background:var(--white);padding:48px 42px}
.hero-card h1{font-weight:800;font-size:66px;line-height:.93;color:var(--slate);letter-spacing:-.5px}
.hero-card h1 span{color:var(--grey)}
.hero-card p{font-size:22px;color:var(--slate);margin-top:12px}
.btns{display:flex;gap:10px;margin-top:18px}
.btn{display:inline-flex;align-items:center;justify-content:center;height:36px;padding:0 22px;border-radius:18px;font-size:11px;font-weight:600;letter-spacing:.2px}
.btn-blue{background:var(--blue);color:var(--white)}
.btn-line{border:2px solid var(--slate);color:var(--slate)}
.play{left:909px;top:643px;width:120px;height:120px;border-radius:50%;background:var(--blue);display:flex;align-items:center;justify-content:center}

/* welcome */
.mark-area{left:198px;top:819px;width:355px;height:254px;display:flex;align-items:center;justify-content:center;gap:14px;font-weight:800;font-size:52px;color:var(--slate)}
.mark-area .sq{width:40px;height:40px;background:var(--grey)}
.eyebrow{left:627px;top:813px;font-size:11px;font-weight:600;color:var(--slate);display:flex;align-items:center;gap:10px}
.eyebrow::before{content:"";width:36px;height:1px;background:#c9ced4}
.welcome-title{left:622px;top:828px;font-weight:800;font-size:35px;color:var(--slate)}
.welcome-title span{color:var(--grey)}
.welcome-text{left:624px;top:888px;width:390px;font-size:13.5px;line-height:22px}
.welcome-call{left:624px;top:989px;font-size:13.5px}
.welcome-btn{left:623px;top:1037px;height:36px;width:129px;padding:0}
.divider{left:89px;top:1150px;width:1021px;height:1px;background:var(--line)}

/* services */
.band{left:0;top:1710px;width:1200px;height:586px;background:var(--band)}
.section-title{width:1200px;left:0;text-align:center;font-weight:800;font-size:38px;color:var(--slate)}
.section-title span{color:var(--grey)}
.services-intro{left:240px;top:1262px;width:720px;text-align:center;font-size:14px;line-height:22px}
.card{width:265px;height:213px;background:var(--white);box-shadow:0 10px 30px rgba(40,60,80,.08);padding:30px 30px}
.card h3{font-size:19px;font-weight:600;color:var(--slate)}
.card p{font-size:11.5px;line-height:18px;margin-top:12px;height:54px}
.card a{display:inline-block;margin-top:26px;font-size:10.5px;font-weight:600;color:var(--grey);border-bottom:1px solid var(--grey);letter-spacing:.2px}

/* projects */
.project{width:501px;height:447px;display:flex;align-items:flex-end;justify-content:center;padding-bottom:30px}
.project h3{font-size:22px;font-weight:700;color:var(--white);position:relative}
.project .art{position:absolute;left:80px;top:30px;right:80px;height:320px;border-radius:24px}
.p1{left:89px;top:1970px;background:var(--slate-deep)}
.p1 .art{background:linear-gradient(135deg,#f2b28a 0%,#eef1f3 45%,#d9dde1 100%);opacity:.9}
.p2{left:609px;top:1970px;background:#8e98a6}
.p2 .art{background:linear-gradient(135deg,#7c6fae 0%,#e6e9ee 50%,#c9465e 100%);opacity:.85}
.view-all{left:523px;top:2466px;width:154px;height:36px;padding:0}

/* clients */
.clients-title{left:183px;top:2582px;font-weight:800;font-size:36px;color:var(--slate)}
.clients-title span{color:var(--grey)}
.clients-text{left:183px;top:2644px;width:460px;font-size:13.5px;line-height:20px}
.clients-text p+p{margin-top:9px}
.client-cap{left:183px;top:2808px;font-size:11.5px;font-weight:600;color:var(--slate);line-height:18px}
.dots{left:183px;top:2869px;display:flex;gap:10px}
.dots i{width:9px;height:9px;border-radius:50%;background:#c4cad1}
.dots i:first-child{background:var(--slate)}
.client-circle{left:703px;top:2586px;width:274px;height:274px;border-radius:50%;background:var(--white);box-shadow:0 15px 40px rgba(40,60,80,.1);display:flex;align-items:center;justify-content:center;gap:10px;font-size:26px;font-weight:600;color:#6f7f3a}
.client-circle .sq{width:18px;height:18px;border-radius:50%;background:#6f7f3a}
.quote{left:905px;top:2555px}

/* cta + footer */
.footer{left:0;top:3079px;width:1200px;height:569px;background:var(--slate-deep)}
.cta{left:89px;top:2969px;width:1023px;height:231px;background:var(--blue)}
.cta h2{position:absolute;left:87px;top:62px;font-weight:800;font-size:35px;color:var(--white)}
.cta p{position:absolute;left:87px;top:124px;width:640px;font-size:13.5px;line-height:23px;color:var(--white);font-weight:500}
.cta-btn{left:921px;top:3053px;width:191px;height:63px;border-radius:32px 0 0 32px;background:var(--white);color:var(--slate);font-size:14px;font-weight:600;display:flex;align-items:center;justify-content:center;gap:14px}
.f-brand{left:88px;top:3370px;font-size:30px;font-weight:600;color:var(--white);letter-spacing:1px;display:flex;align-items:center;gap:12px}
.f-brand span{color:var(--grey)}
.f-brand .sq{width:20px;height:20px;background:var(--grey)}
.f-head{font-size:19px;font-weight:600;color:var(--white)}
.f-links{left:414px;top:3340px;list-style:none;font-size:12.5px;color:#dfe4e8}
.f-links li{height:31px;display:flex;align-items:center;gap:10px}
.f-links li::before{content:"›";font-size:15px}
.f-contact{left:604px;top:3343px;font-size:12.5px;color:#dfe4e8;line-height:18px}
.f-contact .row{display:flex;gap:10px;margin-bottom:20px}
.f-contact .row b{font-weight:400;display:block}
.f-news-text{left:851px;top:3351px;width:260px;font-size:12.5px;line-height:18px;color:#dfe4e8}
.f-input{left:852px;top:3399px;width:258px;height:43px;border-radius:22px;background:var(--white);display:flex;align-items:center;padding:0 18px;gap:8px;font-size:12px;color:#99a2ab}
.f-input svg:last-child{margin-left:auto}
.f-rule{left:89px;top:3588px;width:1021px;height:1px;background:rgba(255,255,255,.15)}
.copyright{left:0;width:1200px;top:3610px;text-align:center;font-size:12px;font-weight:500;color:var(--white)}
.to-top{left:1134px;top:3568px;width:42px;height:42px;border-radius:50%;background:#8e98a6;display:flex;align-items:center;justify-content:center}
</style>
</head>
<body>

<header>
  <div class="abs hero" role="img" aria-label="Aerial video of a harvester working a green crop field"></div>
  <a class="abs brand" href="#"><i class="dot"></i>BRIGHT QUILL</a>
  <nav class="abs nav">
    <a class="active" href="#">HOME</a><a href="#">SERVICES</a><a href="#">PROJECTS</a><a href="#">ABOUT US</a><a href="#">CONTACT</a><a href="#">THOUGHTS</a>
  </nav>
  <div class="abs search"><svg width="16" height="16" viewBox="0 0 16 16" fill="none" stroke="#fff" stroke-width="2"><circle cx="7" cy="7" r="5"/><path d="M11 11l4 4"/></svg></div>
  <div class="abs hero-card">
    <h1>Bright<br><span>Quill</span></h1>
    <p>Web &amp; Mobile Apps</p>
    <div class="btns"><a class="btn btn-blue" href="#">CONTACT US</a><a class="btn btn-line" href="#">RENDER QUOTE</a></div>
  </div>
  <div class="abs play"><svg width="22" height="24" viewBox="0 0 22 24"><path d="M2 2l18 10L2 22z" fill="#fff"/></svg></div>
</header>

<section class="welcome">
  <div class="abs mark-area"><i class="sq"></i>Bright Quill</div>
  <div class="abs eyebrow">WELCOME TO</div>
  <h2 class="abs welcome-title">Bright <span>Quill</span></h2>
  <p class="abs welcome-text">Bright Quill® is all about creating software smarter by providing a senior expert in each area of the project. With our long experience, we know how to make software better, smarter and faster.</p>
  <p class="abs welcome-call">Give us a call or send a message.</p>
  <a class="abs btn btn-line welcome-btn" href="#">RENDER QUOTE</a>
  <div class="abs divider"></div>
</section>

<div class="abs band"></div>

<section class="services">
  <h2 class="abs section-title" style="top:1200px">Some of Our <span>Services</span></h2>
  <p class="abs services-intro">Bright Quill® provide senior resources in a vast range of areas within system development. Lately, most of our work has been within the fields of app and web development.</p>
  <article class="abs card" style="left:177px;top:1350px"><h3>Web development</h3><p>We provide mainly Nimbus based solutions for small or large projects. Be it one-pagers...</p><a href="#">READ MORE</a></article>
  <article class="abs card" style="left:468px;top:1350px"><h3>Post-Launch support</h3><p>We offer maintenance for websites and mobile apps. After launch, the journey is not...</p><a href="#">READ MORE</a></article>
  <article class="abs card" style="left:759px;top:1350px"><h3>Design and UX</h3><p>Due to our Bright Quill concept we have only the best senior designers working for...</p><a href="#">READ MORE</a></article>
  <article class="abs card" style="left:177px;top:1588px"><h3>App development</h3><p>From design to development to testing and support. We take care of the entire process of...</p><a href="#">READ MORE</a></article>
  <article class="abs card" style="left:468px;top:1588px"><h3>Nimbus CMS</h3><p>We provide mainly Nimbus based solutions for small or large projects. Be it one-pagers...</p><a href="#">READ MORE</a></article>
  <article class="abs card" style="left:759px;top:1588px"><h3>Nimbus CMS</h3><p>Nimbus has a cluster of cutting-edge features which makes it reasonable for the...</p><a href="#">READ MORE</a></article>
</section>

<section class="projects">
  <h2 class="abs section-title" style="top:1887px">Latest <span>Projects</span></h2>
  <a class="abs project p1" href="#"><div class="art" role="img" aria-label="Website page mockups on a warm gradient shape"></div><h3>Website For Accounting Firm</h3></a>
  <a class="abs project p2" href="#"><div class="art" role="img" aria-label="Phone screens of a ticket scanning app on a purple and red shape"></div><h3>Event Ticket Scanning App</h3></a>
  <a class="abs btn btn-line view-all" href="#">VIEW ALL PROJECTS</a>
</section>

<section class="clients">
  <h2 class="abs clients-title">Our <span>Clients</span></h2>
  <div class="abs clients-text">
    <p>As far as agricultural machinery is concerned, it is of great importance that maintenance is carried out in accordance with the manufacturer's recommendations. It affects both the resale value and the operating cost.</p>
    <p>Bright Quill has been involved from the planning stage and now delivers a complete app linked to business systems and Cirrus Identity B2C.</p>
  </div>
  <p class="abs client-cap">Service App for farming equipment<br>Fieldhands AB</p>
  <div class="abs dots"><i></i><i></i><i></i></div>
  <div class="abs client-circle"><i class="sq"></i>Fieldhands</div>
  <svg class="abs quote" width="112" height="98" viewBox="0 0 112 98" fill="#2f4a5a"><path d="M0 70a26 26 0 1 0 26-26c0-16 8-30 26-38L46 0C18 10 0 34 0 70z"/><path d="M60 70a26 26 0 1 0 26-26c0-16 8-30 26-38l-6-6C78 10 60 34 60 70z"/></svg>
</section>

<footer>
  <div class="abs footer"></div>
  <div class="abs cta">
    <h2>Bright Quill® Request For Quote</h2>
    <p>Start the exciting journey of creating a mobile app or website by submitting a request for a quote. Requests are handled quickly and with integrity.</p>
  </div>
  <a class="abs cta-btn" href="#">RENDER QUOTE <svg width="8" height="12" viewBox="0 0 8 12" fill="none" stroke="#2f4a5a" stroke-width="2"><path d="M1 1l5 5-5 5"/></svg></a>

  <div class="abs f-brand"><i class="sq"></i>BRIGHT <span>QUILL</span></div>
  <h4 class="abs f-head" style="left:414px;top:3292px">Quick links</h4>
  <ul class="abs f-links"><li>Home</li><li>Services</li><li>Projects</li><li>About Us</li><li>Contact</li><li>Our Thoughts &amp; News</li></ul>
  <h4 class="abs f-head" style="left:604px;top:3292px">Contact info</h4>
  <div class="abs f-contact">
    <div class="row"><svg width="12" height="12" viewBox="0 0 12 12" fill="#8b95a1"><rect y="2" width="12" height="8" rx="1"/></svg><div><b>Email:</b>info@brightquill.eu</div></div>
    <div class="row"><svg width="12" height="12" viewBox="0 0 12 12" fill="#8b95a1"><path d="M2 1l3 0 1 3-2 1a7 7 0 0 0 3 3l1-2 3 1v3c-6 0-10-4-10-9z"/></svg><div><b>Phone:</b>+46 (0)40 123 45 00</div></div>
    <div class="row"><svg width="12" height="14" viewBox="0 0 12 14" fill="#8b95a1"><path d="M6 0a5 5 0 0 1 5 5c0 4-5 9-5 9S1 9 1 5a5 5 0 0 1 5-5z"/></svg><div><b>Location:</b>Lindgatan 4<br>211 40 Malmö, Sweden</div></div>
  </div>
  <h4 class="abs f-head" style="left:851px;top:3294px">Newsletter</h4>
  <p class="abs f-news-text">Sign up for the Bright Quill newsletter and get the latest news and offers sent</p>
  <div class="abs f-input"><svg width="12" height="10" viewBox="0 0 12 10" fill="#99a2ab"><rect width="12" height="10" rx="1"/></svg>Enter Your Email...<svg width="16" height="14" viewBox="0 0 16 14" fill="#0aa1f0"><path d="M0 6L16 0 12 14 8 9z"/></svg></div>
  <div class="abs f-rule"></div>
  <p class="abs copyright">© 2022 Bright Quill | All Rights Reserved | Cookies and Privacy policy</p>
  <div class="abs to-top"><svg width="10" height="14" viewBox="0 0 10 14" fill="none" stroke="#fff" stroke-width="1.5"><path d="M5 13V1M1 5l4-4 4 4"/></svg></div>
</footer>

</body>
</html>
```